Masculine, visually appealing sales presentation for CPA firm

I have a basic power point that I use for sales presentations and I would like it to be updated to be more appealing and modern.

This is a presentation I give to real estate agents to help them close sales, save taxes, and resolve tax disputes. I would like the powerpoint to be updated to be more visually appealing. I have included the current powerpoint along with some of my logo files.

You don't have to use any of the pictures/clip art that is in the current power point. I only care that the words of the powerpoint make it to the new version.

Target Market(s)

Realtors, Real Estate Agents

Industry/Entity Type

Accounting

Requirements
Must have
• Visually appealing. I don't want it to look like I just took a template and made a normal powerpoint out of it. It should look custom.
Should not have
• Anything unprofessional, anything inconsistent with my brand

```html
<!DOCTYPE html>
<html lang="en">
<head>
<meta charset="UTF-8">
<title>Table of Contents – Part 1</title>
<link href="https://fonts.googleapis.com/css2?family=Oswald:wght@300&display=swap" rel="stylesheet">
<style>
  :root {
    --stage-dark: #252525;
    --panel-amber: #d4973a;
    --ink-light: #ffffff;
    --footer-bg: #ffffff;
    --footer-ink: #111111;
  }
  html, body {
    margin: 0;
    padding: 0;
    overflow: hidden;
  }
  body {
    width: 1200px;
    height: 900px;
    font-family: 'Oswald', 'Arial Narrow', sans-serif;
    font-weight: 300;
  }
  .slide {
    position: relative;
    width: 1200px;
    height: 900px;
    background: var(--stage-dark);
    overflow: hidden;
  }
  .content-panel {
    position: absolute;
    left: 258px;
    top: 0;
    width: 684px;
    height: 842px;
    background: var(--panel-amber);
    color: var(--ink-light);
  }
  .slide-title {
    position: absolute;
    top: 58px;
    left: 0;
    width: 100%;
    margin: 0;
    text-align: center;
    font-weight: 300;
    font-size: 48px;
    line-height: 60px;
    letter-spacing: 2px;
  }
  .section-heading {
    position: absolute;
    top: 278px;
    left: 28px;
    margin: 0;
    font-weight: 300;
    font-size: 38px;
    letter-spacing: 2px;
  }
  .topic-list {
    position: absolute;
    top: 408px;
    left: 28px;
    margin: 0;
    padding: 0;
    list-style: none;
  }
  .topic-list li {
    position: relative;
    padding-left: 60px;
    height: 83px;
    font-size: 39px;
    line-height: 56px;
    letter-spacing: 1.6px;
  }
  .topic-list li::before {
    content: "-";
    position: absolute;
    left: 4px;
    top: 0;
    font-size: 22px;
  }
  .footer-bar {
    position: absolute;
    left: 0;
    top: 842px;
    width: 1200px;
    height: 58px;
    background: var(--footer-bg);
    display: flex;
    align-items: center;
    color: var(--footer-ink);
  }
  .firm-name {
    margin-left: 42px;
    width: 338px;
    font-size: 22px;
    letter-spacing: 1px;
  }
  .society-name {
    font-size: 21px;
    letter-spacing: 0.8px;
  }
</style>
</head>
<body>
  <main class="slide">
    <section class="content-panel">
      <h1 class="slide-title">TABLE OF CONTENTS<br>PART 1</h1>
      <h2 class="section-heading">TAXATION&nbsp; AND CLIENT</h2>
      <ul class="topic-list">
        <li>SALE OF PRINCIPAL RESIDENCE</li>
        <li>FEDERAL TAX LIEN ON REAL ESTATE</li>
        <li>CANCELLATION OF DEBT</li>
      </ul>
    </section>
    <footer class="footer-bar">
      <div class="firm-name">HARWELL TAX ADVISORS</div>
      <div class="society-name">NATIONAL GUILD OF TAX RESOLVERS©</div>
    </footer>
  </main>
</body>
</html>
```